New Business card design to reflect rebrand

I would like a business card design with a good base colour for our new logo and also a placeholder for a profile pic of the card holder. the design needs to be editable to the point that we can easily change the picture of the person and use that design for printlarkly etc. we are looking at a metalic finish business card so will need a good base colour to bring out the finish.

Target Market(s)

prospective customers

Industry/Entity Type

Business

Contact Information for Business Card

I would like one editable design that we can change the name of the card holder and profile picture. The design need to be in a format that be send to printlarkly etc.

Our address is Fenwick Lodge, Mill Lane, Ashcombe Vale, KT14 3WB Tel no. 01632 960418

Requirements
Must have
• place holder for a profile pic for the card holder. in AI or preferably PSD format

```html
<!DOCTYPE html>
<html lang="en">
<head>
<meta charset="utf-8">
<title>Corvane Workplace Services – Business Card</title>
<link rel="stylesheet" href="https://fonts.googleapis.com/css2?family=Open+Sans:wght@400;600;800&display=swap">
<style>
  :root {
    --bg: #e9e6e1;
    --metal-light: #e4e4e4;
    --metal-mid: #bdbdbd;
    --metal-dark: #8c8c8c;
    --ink: #161616;
    --ink-soft: #2c2c2c;
    --band: #0d0d0d;
    --band-edge: #6b6b6b;
    --photo-dark: #4a4a4a;
    --photo-mid: #6e6e6e;
    --white: #ffffff;
  }
  * { box-sizing: border-box; margin: 0; padding: 0; }
  html, body { width: 1200px; height: 843px; overflow: hidden; }
  body {
    background: var(--bg);
    font-family: "Open Sans", Arial, sans-serif;
    position: relative;
  }
  .card {
    position: absolute;
    width: 600px;
    height: 343px;
    overflow: hidden;
    background: linear-gradient(120deg, var(--metal-mid) 0%, var(--metal-light) 38%, var(--metal-mid) 62%, var(--metal-dark) 100%);
    box-shadow: 0 6px 18px rgba(0,0,0,0.25);
  }
  .card--back { left: 80px; top: 70px; }
  .card--front { left: 520px; top: 430px; }

  /* back */
  .back-name {
    position: absolute; left: 0; right: 0; top: 112px;
    text-align: center;
    font-weight: 800; font-size: 64px; letter-spacing: 2px;
    color: var(--ink);
  }
  .back-url {
    position: absolute; left: 0; right: 0; top: 200px;
    text-align: center;
    font-size: 15px; letter-spacing: 9px;
    color: var(--ink-soft);
  }

  /* front */
  .brand { position: absolute; left: 150px; top: 26px; text-align: center; }
  .brand-name {
    font-weight: 800; font-size: 38px; letter-spacing: 2px; line-height: 1;
    color: var(--ink);
  }
  .brand-tag {
    margin-top: 4px;
    font-size: 12.5px; letter-spacing: 3.2px;
    color: var(--ink-soft);
  }
  .address {
    position: absolute; left: 46px; top: 132px;
    font-size: 15px; line-height: 20px; font-style: normal;
    color: var(--ink-soft);
  }
  .phone {
    position: absolute; left: 46px; top: 218px;
    display: flex; align-items: center; gap: 8px;
    font-size: 15px; color: var(--ink-soft);
  }
  .phone svg { width: 13px; height: 13px; }
  .profile-photo {
    position: absolute; left: 350px; top: 105px;
    width: 215px; height: 200px;
    background: linear-gradient(180deg, var(--photo-mid) 0%, var(--photo-dark) 100%);
  }
  .name-band { position: absolute; left: 0; bottom: 0; width: 600px; height: 70px; }
  .holder {
    position: absolute; right: 22px; bottom: 14px;
    font-size: 19px; color: var(--white); white-space: nowrap;
  }
  .holder-name { font-weight: 600; }
  .holder-role { font-size: 15px; }
</style>
</head>
<body>

<section class="card card--back" aria-label="Card back">
  <div class="back-name">CORVANE</div>
  <div class="back-url">WWW.CORVANE.COM</div>
</section>

<section class="card card--front" aria-label="Card front">
  <div class="brand">
    <div class="brand-name">CORVANE</div>
    <div class="brand-tag">WORKPLACE SERVICES</div>
  </div>

  <address class="address">
    Fenwick Lodge<br>
    Mill Lane, Ashcombe Vale<br>
    KT14 3WB
  </address>

  <div class="phone">
    <svg viewBox="0 0 24 24" aria-hidden="true"><path fill="#1a1a1a" d="M6.6 10.8a15 15 0 0 0 6.6 6.6l2.2-2.2a1 1 0 0 1 1-.25 11.4 11.4 0 0 0 3.6.57 1 1 0 0 1 1 1V20a1 1 0 0 1-1 1A17 17 0 0 1 3 4a1 1 0 0 1 1-1h3.5a1 1 0 0 1 1 1c0 1.25.2 2.45.57 3.6a1 1 0 0 1-.25 1z"/></svg>
    <span>01632 960418</span>
  </div>

  <div class="profile-photo" role="img" aria-label="Profile photo placeholder of the card holder"></div>

  <svg class="name-band" viewBox="0 0 600 70" aria-hidden="true">
    <polygon points="0,44 600,14 600,70 0,70" fill="var(--band-edge)"/>
    <polygon points="250,38 600,14 600,70 220,70" fill="var(--band)"/>
  </svg>
  <div class="holder"><span class="holder-name">Alex Morgan</span> - <span class="holder-role">CEO/Founder</span></div>
</section>

</body>
</html>
```